vacuumfood jar modern packaging for design product

the design should be modern and simple. As seen in the target market, the jar can be used by mothers for their babies, but also for workers in offices and outdoor fanatics. package dimensions: 10.5 x 10.5 x 17.0 cm

Target Market(s)

food jar for mothers / baby food on the other hand modern design for food jars in everday use (work, outdoors, ...)

Industry/Entity Type

Product

Font styles to use
Sans Serif

Colors

Designer to choose colors to be used in the design.

Requirements
Must have
• We would like to have one side in german and one side in english front: Calendo Food Jar (thermo food container) back: vacuum food jar information / characteristics: no BPA stainless steel copper coating hot / cold for up to 24 h (see example hot cold.pic) - voblo logo - www.voblo.eu - symbol "food contact material" - EAN barcode - 450 ml / 15,2 oz importanp: do not microwave, not for dishwasher - can be pictograms / icons
Should not have
• No picture of the real product on the package

```html
<!DOCTYPE html>
<html lang="en">
<head>
<meta charset="utf-8">
<title>voblo Vacuum Food Jar – Packaging Sides</title>
<link rel="stylesheet" href="https://fonts.googleapis.com/css2?family=Roboto:wght@300;400&family=Roboto+Condensed:wght@300;400&display=swap">
<style>
  :root {
    --orange: #f47920;
    --grey: #b3b3b3;
    --grey-dark: #9a9a9a;
    --white: #ffffff;
    --ink: #6d6d6d;
    --stage: #ececec;
  }
  * { box-sizing: border-box; margin: 0; padding: 0; }
  html, body { width: 1200px; height: 669px; overflow: hidden; }
  body {
    background: var(--stage);
    font-family: "Roboto", sans-serif;
    display: flex;
    align-items: center;
    justify-content: center;
    gap: 40px;
  }
  .side {
    width: 320px;
    height: 520px;
    display: flex;
    flex-direction: column;
    box-shadow: 0 2px 8px rgba(0,0,0,0.08);
  }
  .side__band {
    height: 86px;
    display: flex;
    align-items: flex-end;
    padding: 0 0 14px 20px;
  }
  .brand-name {
    font-family: "Roboto", sans-serif;
    font-weight: 300;
    font-size: 34px;
    color: var(--white);
    letter-spacing: 0.5px;
  }
  .side__body {
    flex: 1;
    position: relative;
  }
  .side--german .side__band { background: var(--grey); }
  .side--german .side__body { background: var(--orange); }
  .side--english .side__band { background: var(--orange); }
  .side--english .side__body { background: var(--grey); }
  .side--info .side__band { background: var(--orange); justify-content: flex-end; padding-right: 20px; }
  .side--info .side__body { background: var(--white); }

  .jar-artwork {
    position: absolute;
    left: 40px;
    top: 80px;
    width: 150px;
    height: 230px;
    border-radius: 14px;
    background: linear-gradient(180deg, rgba(255,255,255,0.28), rgba(255,255,255,0.12));
  }
  .title-block {
    position: absolute;
    right: 22px;
    bottom: 24px;
    writing-mode: vertical-rl;
    transform: rotate(180deg);
    color: var(--white);
    display: flex;
    gap: 4px;
  }
  .title-block__main { font-size: 27px; font-weight: 400; letter-spacing: 1px; }
  .title-block__sub { font-size: 19px; font-weight: 300; letter-spacing: 1px; }

  .info-jar {
    position: absolute;
    left: 18px;
    top: 24px;
    width: 80px;
    height: 150px;
    border-radius: 8px;
    background: linear-gradient(180deg, #e2e2e2, #d2d2d2);
  }
  .info-text {
    position: absolute;
    left: 118px;
    top: 24px;
    right: 14px;
    font-family: "Roboto Condensed", sans-serif;
    font-weight: 300;
    color: var(--ink);
    font-size: 12px;
    line-height: 1.75;
  }
  .info-text__heading { font-weight: 400; font-size: 12px; margin-bottom: 2px; }
  .temp-badges { display: flex; gap: 8px; margin-top: 18px; }
  .temp-badge {
    border: 1.5px solid var(--ink);
    border-radius: 4px;
    padding: 2px 6px;
    font-size: 10px;
    line-height: 1.2;
  }
  .temp-badge--hot { color: var(--orange); border-color: var(--ink); }
  .volume { margin-top: 22px; font-size: 17px; }
  .important { margin-top: 22px; font-weight: 400; font-size: 11px; }
  .pictograms {
    position: absolute;
    right: 12px;
    bottom: 30px;
    display: flex;
    gap: 8px;
  }
  .pictogram { display: flex; flex-direction: column; align-items: center; gap: 4px; }
  .pictogram__label {
    font-family: "Roboto Condensed", sans-serif;
    font-size: 7px;
    color: var(--ink);
  }
  .web-address {
    position: absolute;
    left: 18px;
    bottom: 40px;
    font-family: "Roboto Condensed", sans-serif;
    font-size: 12px;
    color: var(--ink);
  }
</style>
</head>
<body>

  <section class="side side--german" lang="de">
    <div class="side__band"><span class="brand-name">voblo</span></div>
    <div class="side__body">
      <div class="jar-artwork" role="img" aria-label="Line illustration of a vacuum food jar with handle"></div>
      <div class="title-block">
        <span class="title-block__main">CALENDO SPEISEBEHÄLTER</span>
        <span class="title-block__sub">CALENDO SPEISE BEHÄLTER</span>
      </div>
    </div>
  </section>

  <section class="side side--english">
    <div class="side__band"><span class="brand-name">voblo</span></div>
    <div class="side__body">
      <div class="jar-artwork" role="img" aria-label="Line illustration of a vacuum food jar with handle"></div>
      <div class="title-block">
        <span class="title-block__main">VACUUM FOOD JAR</span>
        <span class="title-block__sub">FOOD JARS FOR EVERDAY USE</span>
      </div>
    </div>
  </section>

  <section class="side side--info">
    <div class="side__band"><span class="brand-name">voblo</span></div>
    <div class="side__body">
      <div class="info-jar" role="img" aria-label="Line illustration of a vacuum food jar"></div>
      <div class="info-text">
        <p class="info-text__heading">INFORMATION</p>
        <p>No BPA</p>
        <p>Stainless steel</p>
        <p>Copper coating for better<br>insulation performance</p>
        <p>Scratch resistance bottom</p>
        <p>Offers non-slip grip</p>
        <p>Keeps hot/cold for up to 24 h</p>
        <div class="temp-badges">
          <span class="temp-badge temp-badge--hot">KEEPS HOT 24h</span>
          <span class="temp-badge">KEEPS COLD 24h</span>
        </div>
        <p class="volume">450 ml / 15,2 oz</p>
        <p class="important">IMPORTANT:</p>
      </div>
      <p class="web-address">www.voblo.eu</p>
      <div class="pictograms">
        <div class="pictogram">
          <svg width="46" height="46" viewBox="0 0 46 46" aria-label="Food contact material">
            <circle cx="23" cy="23" r="21" fill="none" stroke="#6d6d6d" stroke-width="2.5"/>
            <circle cx="23" cy="23" r="10" fill="var(--orange)"/>
          </svg>
          <span class="pictogram__label">food safe</span>
        </div>
        <div class="pictogram">
          <svg width="46" height="46" viewBox="0 0 46 46" aria-label="Do not microwave">
            <circle cx="23" cy="23" r="21" fill="none" stroke="#6d6d6d" stroke-width="2.5"/>
            <rect x="11" y="15" width="24" height="16" rx="2" fill="none" stroke="var(--orange)" stroke-width="2"/>
            <line x1="9" y1="37" x2="37" y2="9" stroke="#6d6d6d" stroke-width="2.5"/>
          </svg>
          <span class="pictogram__label">do not microwave</span>
        </div>
        <div class="pictogram">
          <svg width="46" height="46" viewBox="0 0 46 46" aria-label="Not for dishwasher">
            <circle cx="23" cy="23" r="21" fill="none" stroke="#6d6d6d" stroke-width="2.5"/>
            <rect x="14" y="11" width="18" height="24" rx="2" fill="none" stroke="var(--orange)" stroke-width="2"/>
            <line x1="14" y1="17" x2="32" y2="17" stroke="var(--orange)" stroke-width="2"/>
            <line x1="9" y1="37" x2="37" y2="9" stroke="#6d6d6d" stroke-width="2.5"/>
          </svg>
          <span class="pictogram__label">not for dishwasher</span>
        </div>
      </div>
    </div>
  </section>

</body>
</html>
```